Business Card Design

Attached is the logo of the store.

Information needed on the business card:

www.brookvale17vino.com
info@brookvale17vino.com
412 Harlow St NY, NY 10027
Tel:(646) 472-3958

Store Hours
Mon-Sat Noon-10pm
Sun Noon-8pm

Free Deliveries

Industry/Entity Type

Business

Contact Information for Business Card

Brookvale 17 Wine & Spirits

```html
<!DOCTYPE html>
<html lang="en">
<head>
<meta charset="utf-8">
<title>Brookvale 17 Wine &amp; Spirits — Business Card</title>
<link rel="stylesheet" href="https://fonts.googleapis.com/css2?family=Great+Vibes&family=Parisienne&display=swap">
<style>
  :root {
    --stage: #d6d6d6;
    --card-black: #1f1f1f;
    --card-red: #b8332f;
    --accent-red: #d2262c;
    --ink-white: #f4f4f4;
    --ink-soft: #e2e2e2;
  }
  * { box-sizing: border-box; margin: 0; padding: 0; }
  html, body {
    width: 1200px;
    height: 1000px;
    overflow: hidden;
    background: var(--stage);
  }
  .sheet {
    width: 1200px;
    height: 1000px;
    display: flex;
    flex-direction: column;
    align-items: center;
    justify-content: center;
    gap: 36px;
  }
  .card {
    position: relative;
    width: 780px;
    height: 446px;
    background:
      radial-gradient(ellipse 38% 55% at 100% 0%, var(--card-red) 0%, rgba(184,51,47,0.55) 35%, rgba(184,51,47,0) 75%),
      radial-gradient(ellipse 32% 50% at 0% 100%, var(--card-red) 0%, rgba(184,51,47,0.5) 35%, rgba(184,51,47,0) 75%),
      var(--card-black);
    color: var(--ink-white);
    overflow: hidden;
  }

  /* Back side: hours and delivery */
  .card-back {
    display: flex;
    flex-direction: column;
    align-items: center;
    padding-top: 70px;
  }
  .hours-title {
    font-family: "Parisienne", cursive;
    font-weight: 400;
    font-size: 44px;
    line-height: 1.1;
  }
  .hours-line {
    font-family: "Parisienne", cursive;
    font-size: 32px;
    line-height: 1.35;
    color: var(--ink-soft);
  }
  .delivery {
    font-family: "Great Vibes", cursive;
    font-size: 84px;
    margin-top: 46px;
  }

  /* Front side: name and contact */
  .brand {
    position: absolute;
    left: 80px;
    top: 100px;
    display: flex;
    align-items: center;
    gap: 18px;
  }
  .brand-name {
    font-family: "Parisienne", cursive;
    font-weight: 400;
    font-size: 48px;
    line-height: 1.2;
    white-space: nowrap;
    color: var(--ink-white);
  }
  .brand-dot {
    flex: none;
    width: 34px;
    height: 34px;
    border-radius: 50%;
    background: var(--accent-red);
  }
  .contact {
    position: absolute;
    right: 56px;
    top: 230px;
    font-family: "Parisienne", cursive;
    font-size: 29px;
    line-height: 1.45;
    color: var(--ink-soft);
    list-style: none;
  }
</style>
</head>
<body>
<main class="sheet">
  <section class="card card-back" aria-label="Card back">
    <h2 class="hours-title">Store Hours:</h2>
    <p class="hours-line">Mon-Sat Noon-10pm</p>
    <p class="hours-line">Sun Noon-8pm</p>
    <p class="delivery">Free Deliveries</p>
  </section>

  <section class="card card-front" aria-label="Card front">
    <div class="brand">
      <h1 class="brand-name">Brookvale 17 Wine &amp; Spirits</h1>
      <span class="brand-dot" aria-hidden="true"></span>
    </div>
    <ul class="contact">
      <li>www.brookvale17vino.com</li>
      <li>info@brookvale17vino.com</li>
      <li>412 Harlow St NY, NY 10027</li>
      <li>Tel: (646) 472-3958</li>
    </ul>
  </section>
</main>
</body>
</html>
```